Corporate Identity Pack - LetterHead, Business Card, Envelope

We are looking for a clean, professional, and visually connected corporate identity set for our company "VELTA HOME" (Cleaning, Gardening, and Pest Control services).

The pack must include:

Business Card (front and back)
Envelope with recipient window on the right side (22x11)
A4 Letterhead

We provide:
Our final logo (PNG)
Three design references (Inspiration1, Inspiration2, Inspiration3) to spark ideas — but you are absolutely free to propose your own creative solutions based on these concepts.

What we want:
A clean, modern, and trustworthy style
A subtle but creative watermark or graphic detail on the letterhead (not too invasive)

The same visual "family feeling" across business card, envelope, and letterhead: designs must be different but clearly connected

Strong readability for all text and contact details

Use our brand colors (Navy Blue, Green, Orange/Red) in a smart, non-overloaded way

No strict limitations: we are open to creative proposals as long as they are coherent, elegant, and suitable for professional use

Technical specifications:
100% full A4 page layout (no accidental borders)

Deliver ready-to-print PDFs and vector files (AI, EPS)

Respect 5 mm safety margins

Standard sizes for A4, business card, envelope C6 with window at the right

Tone:
Modern – Clean – Elegant – Creative – Trustworthy

Target Market(s)

Professional businesses, property managers, condominium administrators, companies, clinics, and offices requiring cleaning, gardening, and pest control services. The design must convey trust, reliability, professionalism, and attention to detail.

Industry/Entity Type

Cleaning Services, Gardening Services, Pest Control Services

Colors
0054AA
0677BA
7BADD7
CADEEF
E8F1F8
59FF00
82FF00
B8FF75
E3FFCB
F4FFEA
EB3D1F
EC4F4E
F09395
F8D3D4
FCEDEE

Requirements
Must have
• Cohesive design across business card, letterhead, and envelope Clean, modern, professional look Use of brand colors: Navy Blue (main), Green, Orange/Red accents Letterhead must include a subtle watermark without interfering with text Envelope must be with a transparent window for recipient address visibility High readability of all text and contact details Proper alignment, no unnecessary margins (full A4 layout)
Nice to have
• Creative but discreet use of the checkmark from the logo as part of the background or watermark Slight variation or accent of color tones while respecting brand identity A clean visual accent that gives a sense of movement or dynamic professionalism (without being distracting) Icons for email, phone, and website on the business card (if stylistically appropriate)
Should not have
• Overuse of colors or rainbow effects Heavy backgrounds or complex textures that interfere with readability Fonts that are too playful, comic-style, or non-professional Overcrowded layouts — the design must feel clean and spacious Watermarks that are too strong or central (they must be subtle and marginal)

```html
<!DOCTYPE html>
<html lang="en">
<head>
<meta charset="utf-8">
<title>Velta Home – Corporate Identity</title>
<link href="https://fonts.googleapis.com/css2?family=Montserrat:wght@400;500;600;700&display=swap" rel="stylesheet">
<style>
  :root{
    --navy:#16167a;
    --green:#6cc72f;
    --orange:#ff6a0a;
    --ink:#1f1f3a;
    --tint:#f3f8ec;
    --window:#e4e5e7;
    --paper:#ffffff;
  }
  *{box-sizing:border-box;margin:0;padding:0}
  html,body{width:1175px;height:1200px;overflow:hidden;background:#fff}
  body{position:relative;font-family:"Montserrat",Arial,sans-serif;color:var(--ink)}
  .piece{position:absolute;background:var(--paper);box-shadow:0 6px 22px rgba(0,0,0,.16);overflow:hidden}
  .stripe{position:absolute;left:0;right:0;display:flex}
  .stripe span{flex:1}
  .stripe span:nth-child(1){background:var(--navy)}
  .stripe span:nth-child(2){background:var(--green)}
  .stripe span:nth-child(3){background:var(--orange)}
  .tint{position:absolute;left:0;right:0;top:0;background:linear-gradient(180deg,#f0f6e8,var(--tint) 70%,#fbfdf8)}
  .wordmark{position:absolute;font-weight:600;color:var(--navy);letter-spacing:.02em;white-space:nowrap;line-height:1}
  .company{position:absolute;color:var(--navy);line-height:1.45;white-space:nowrap}
  .company strong{display:block;font-weight:700}
  .company b{display:block;font-weight:600}
  .company span{display:block;color:var(--ink)}
  .contacts{position:absolute;list-style:none;line-height:1.45;color:var(--ink)}
  .contacts li{display:flex;align-items:center;gap:.6em;white-space:nowrap}
  .contacts svg{width:1.1em;height:1.1em;flex:none;fill:var(--navy)}
  .badge{flex:none;font-size:.55em;font-weight:700;color:var(--navy);border:1px solid var(--navy);border-radius:1em;padding:0 .3em;line-height:1.3;width:2.3em;text-align:center}

  /* business card back */
  .card-back{left:58px;top:365px;width:284px;height:162px}
  .card-back .stripe{top:5px;height:4px}
  .card-back .tint{height:107px}
  .card-back .wordmark{left:0;right:0;top:44px;text-align:center;font-size:28px}
  .card-back .band{position:absolute;left:0;right:0;bottom:0;height:55px;background:var(--navy)}
  .card-back .url{position:absolute;left:77px;top:17px;width:130px;height:19px;border:1px solid #fff;border-radius:10px;color:#fff;font-size:9px;font-weight:600;display:flex;align-items:center;justify-content:center;white-space:nowrap}

  /* business card front */
  .card-front{left:366px;top:365px;width:283px;height:162px}
  .card-front .tint{height:74px}
  .card-front .wordmark{left:0;right:0;top:28px;text-align:center;font-size:24px}
  .card-front .company{left:14px;top:84px;font-size:6.2px}
  .card-front .company strong{font-size:7px}
  .card-front .contacts{left:180px;top:92px;font-size:6.2px}
  .card-front .stripe{bottom:5px;height:4px}

  /* envelope */
  .envelope{left:58px;top:576px;width:491px;height:246px}
  .envelope .stripe.top{top:8px;height:5px}
  .envelope .stripe.bottom{bottom:8px;height:5px}
  .envelope .tint{height:92px}
  .envelope .wordmark{left:22px;top:38px;font-size:20px}
  .envelope .window{position:absolute;left:263px;top:77px;width:181px;height:91px;border-radius:11px;background:var(--window)}
  .envelope .company{left:22px;top:165px;font-size:7px}
  .envelope .company strong{font-size:7.8px}
  .envelope .contacts.main{left:235px;top:194px;font-size:7px}
  .envelope .contacts.codes{left:373px;top:205px;font-size:7px}

  /* letterhead */
  .letterhead{left:703px;top:319px;width:398px;height:563px}
  .letterhead .stripe.top{top:7px;height:6px}
  .letterhead .stripe.bottom{bottom:8px;height:6px}
  .letterhead .tint{height:78px}
  .letterhead .wordmark{left:25px;top:36px;font-size:17px}
  .letterhead .company{left:25px;top:481px;font-size:5.6px}
  .letterhead .company strong{font-size:6.4px}
  .letterhead .contacts{left:229px;top:489px;font-size:5.6px}
</style>
</head>
<body>
<svg width="0" height="0" style="position:absolute" aria-hidden="true">
  <symbol id="i-phone" viewBox="0 0 24 24"><path d="M6.6 10.8a15 15 0 0 0 6.6 6.6l2.2-2.2c.3-.3.7-.4 1-.2 1.1.4 2.3.6 3.6.6.6 0 1 .4 1 1V20c0 .6-.4 1-1 1A17 17 0 0 1 3 4c0-.6.4-1 1-1h3.5c.6 0 1 .4 1 1 0 1.3.2 2.5.6 3.6.1.3 0 .7-.2 1z"/></symbol>
  <symbol id="i-mail" viewBox="0 0 24 24"><path d="M3 5h18v2l-9 6-9-6zM3 9l9 6 9-6v10H3z"/></symbol>
  <symbol id="i-web" viewBox="0 0 24 24"><path d="M12 2a10 10 0 1 0 0 20 10 10 0 0 0 0-20zm6.9 6h-3a15 15 0 0 0-1.3-3.9A8 8 0 0 1 18.9 8zM12 4c.8 1.2 1.5 2.5 1.9 4h-3.8c.4-1.5 1.1-2.8 1.9-4zM4.3 14a8 8 0 0 1 0-4h3.4a16 16 0 0 0 0 4zm.8 2h3a15 15 0 0 0 1.3 3.9A8 8 0 0 1 5.1 16zm3-8h-3a8 8 0 0 1 4.3-3.9A15 15 0 0 0 8.1 8zM12 20c-.8-1.2-1.5-2.5-1.9-4h3.8c-.4 1.5-1.1 2.8-1.9 4zm2.3-6H9.7a14 14 0 0 1 0-4h4.6a14 14 0 0 1 0 4zm.3 5.9a15 15 0 0 0 1.3-3.9h3a8 8 0 0 1-4.3 3.9zm1.7-5.9a16 16 0 0 0 0-4h3.4a8 8 0 0 1 0 4z"/></symbol>
</svg>

<!-- Business card: back -->
<section class="piece card-back" aria-label="Business card back">
  <div class="tint" role="img" aria-label="Faint pattern of small green tick marks"></div>
  <div class="stripe"><span></span><span></span><span></span></div>
  <div class="wordmark">VELTA HOME</div>
  <div class="band"><div class="url">www.velta.example</div></div>
</section>

<!-- Business card: front -->
<section class="piece card-front" aria-label="Business card front">
  <div class="tint" role="img" aria-label="Faint pattern of small green tick marks"></div>
  <div class="wordmark">VELTA HOME</div>
  <div class="company">
    <strong>Velta Home srl</strong>
    <b>Società unipersonale - Einzelunternehmen</b>
    <span>Via dei Tigli 8 - Lindenweg 8</span>
    <span>I-39100 Borgo Nuovo (Bz)</span>
    <span>REA - VWV Nr. Bz 100234</span>
    <span>P.I. - MwSt. 01234567890</span>
  </div>
  <ul class="contacts">
    <li><svg><use href="#i-phone"/></svg>+39 320 555 0147</li>
    <li><svg><use href="#i-mail"/></svg>office@velta.example</li>
    <li><svg><use href="#i-web"/></svg>www.velta.example</li>
    <li><span class="badge">PEC</span>velta@pec.example</li>
    <li><span class="badge">SDI</span>X7QLBT4</li>
  </ul>
  <div class="stripe"><span></span><span></span><span></span></div>
</section>

<!-- Envelope -->
<section class="piece envelope" aria-label="Envelope with window">
  <div class="tint" role="img" aria-label="Faint pattern of small green tick marks"></div>
  <div class="stripe top"><span></span><span></span><span></span></div>
  <div class="wordmark">VELTA HOME</div>
  <div class="window"></div>
  <div class="company">
    <strong>Velta Home srl</strong>
    <b>Società unipersonale - Einzelunternehmen</b>
    <span>Via dei Tigli 8 - Lindenweg 8</span>
    <span>I-39100 Borgo Nuovo (Bz)</span>
    <span>REA - VWV Nr. Bz 100234</span>
    <span>P.I. - MwSt. 01234567890</span>
  </div>
  <ul class="contacts main">
    <li><svg><use href="#i-phone"/></svg>+39 320 555 0147</li>
    <li><svg><use href="#i-mail"/></svg>office@velta.example</li>
    <li><svg><use href="#i-web"/></svg>www.velta.example</li>
  </ul>
  <ul class="contacts codes">
    <li><span class="badge">PEC</span>velta@pec.example</li>
    <li><span class="badge">SDI</span>X7QLBT4</li>
  </ul>
  <div class="stripe bottom"><span></span><span></span><span></span></div>
</section>

<!-- Letterhead -->
<section class="piece letterhead" aria-label="A4 letterhead">
  <div class="tint" role="img" aria-label="Faint pattern of small green tick marks"></div>
  <div class="stripe top"><span></span><span></span><span></span></div>
  <div class="wordmark">VELTA HOME</div>
  <div class="company">
    <strong>Velta Home srl</strong>
    <b>Società unipersonale - Einzelunternehmen</b>
    <span>Via dei Tigli 8 - Lindenweg 8</span>
    <span>I-39100 Borgo Nuovo (Bz)</span>
    <span>REA - VWV Nr. Bz 100234</span>
    <span>P.I. - MwSt. 01234567890</span>
  </div>
  <ul class="contacts">
    <li><svg><use href="#i-phone"/></svg>+39 320 555 0147</li>
    <li><svg><use href="#i-mail"/></svg>office@velta.example</li>
    <li><svg><use href="#i-web"/></svg>www.velta.example</li>
    <li><span class="badge">PEC</span>velta@pec.example</li>
    <li><span class="badge">SDI</span>X7QLBT4</li>
  </ul>
  <div class="stripe bottom"><span></span><span></span><span></span></div>
</section>
</body>
</html>
```